Re-design of veterinary clinic website *

For a future relaunch of our webpage, we would like to find a fresh design that still incorporates the spirit of our current one which can be found at http://dr-wenzlaff.de
We are a small business that appeals to locals but are known in a wide area for specialist services.
According to analytics data, most people rarely read through the full website but are using it to inform themselves about opening hours, Telephone numbers and location. Still, the website needs to offer enough content to be ranked positively by the Quandle algorithm.
Our logo is not part of the re-design but needs to be included in your proposal as is. It can be used a source of inspiration, just as the current design. Keep in mind, that the design will be used as the basis of a fluid webdesign for both mobile and desktop. Roughly 75% of our users are on mobile devices.
Target Market(s)
Locals
Industry/Entity Type
Veterinary
Number of Pages Required
1 page
Look and feel
Each slider illustrates characteristics of the customer's brand and the style your logo design should communicate.

```html
<!DOCTYPE html>
<html lang="de">
<head>
<meta charset="utf-8">
<title>Tierarztpraxis Dr. Wenzlaff – Desktop und Mobil</title>
<link href="https://fonts.googleapis.com/css2?family=Ubuntu:wght@400;500;700&display=swap" rel="stylesheet">
<style>
:root{
  --stage:#d3e1ed;
  --blue:#0a56a8;
  --nav:#1b52a8;
  --nav-active:#2f7fd3;
  --gold:#b9a468;
  --pill:#6fb8e2;
  --track:#e8e9ec;
  --text:#5b5f66;
  --white:#fff;
}
*{box-sizing:border-box;margin:0;padding:0}
html,body{width:1200px;height:1200px;overflow:hidden}
body{background:var(--stage);font-family:"Ubuntu",sans-serif;color:var(--text);position:relative}
.screen{position:absolute;background:var(--white);overflow:hidden;box-shadow:0 10px 30px rgba(40,70,110,.18)}
.abs{position:absolute}

/* desktop */
.desktop{left:102px;top:127px;width:705px;height:945px}
.desktop .hero-photo{left:300px;top:0;width:405px;height:314px}
.desktop .header{left:82px;top:0;width:544px;height:61px;background:var(--white);border-radius:0 0 6px 6px;box-shadow:0 3px 8px rgba(0,0,0,.12)}
.brand{display:flex;align-items:center;gap:6px;color:var(--blue);font-weight:500}
.desktop .brand{left:48px;top:14px;font-size:14px}
.brand .mark{width:9px;height:9px;border-radius:50%;background:var(--blue)}
.desktop .phone{left:418px;top:22px;font-size:8px;color:var(--blue);display:flex;align-items:center;gap:5px}
.nav{left:126px;top:51px;width:452px;height:31px;background:var(--nav);display:flex;align-items:center;font-size:8.5px;color:var(--white);letter-spacing:.2px}
.nav span{padding:0 12px;height:100%;display:flex;align-items:center}
.nav .active{background:var(--nav-active);padding:0 7px}
.desktop .welcome{left:82px;top:117px;width:240px;font-size:11.5px;line-height:17.6px}
.welcome b{color:var(--blue);font-weight:500;font-size:14px}
.btn{background:var(--gold);color:var(--white);font-weight:500;display:flex;align-items:center;justify-content:center;border-radius:2px}
.desktop .btn{left:128px;top:250px;width:124px;height:31px;font-size:12px;letter-spacing:.3px}
.band{background:var(--blue);color:var(--white)}
.desktop .band{left:0;top:314px;width:705px;height:238px}
.desktop .band h2{position:absolute;left:0;right:0;top:22px;text-align:center;font-size:12px;font-weight:500;padding-left:2px}
.row{position:absolute;background:var(--track)}
.day{position:absolute;left:0;top:0;height:100%;background:var(--gold);color:var(--white);display:flex;align-items:center;clip-path:polygon(0 0,86% 0,100% 50%,86% 100%,0 100%)}
.pill{position:absolute;top:0;height:100%;background:var(--pill);color:var(--white);border-radius:6px;display:flex;align-items:center;justify-content:center}
.desktop .row{left:221px;width:264px;height:20px;border-radius:0 6px 6px 0}
.desktop .day{width:92px;padding-left:12px;font-size:11px}
.desktop .p1{left:112px;width:58px;font-size:9.5px}
.desktop .p2{left:197px;width:67px;font-size:9.5px}
.desktop .short{width:170px}
.desktop .k-title{left:0;right:0;top:574px;text-align:center;font-size:12px;font-weight:500;color:#4a4d52}
.desktop .map{left:266px;top:607px;width:358px;height:251px}
.info{background:var(--blue);color:var(--white)}
.desktop .info{left:82px;top:663px;width:184px;height:150px;padding:18px 0 0 22px;font-size:10.5px;line-height:15.5px}
.footer{left:0;width:100%;background:var(--blue);color:var(--white);font-weight:500;display:flex;align-items:center;justify-content:center}
.desktop .footer{top:901px;height:44px;font-size:12px}

/* mobile */
.mobile{left:896px;top:128px;width:189px;height:694px}
.mobile .topbar{left:0;top:0;width:189px;height:12px;background:var(--blue);color:var(--white);font-size:5.5px;display:flex;align-items:center;justify-content:flex-end;gap:3px;padding-right:8px}
.mobile .brand{left:6px;top:22px;font-size:8px}
.mobile .brand .mark{width:6px;height:6px}
.mobile .hero-photo{left:0;top:48px;width:189px;height:90px}
.mobile .burger{left:157px;top:42px;width:32px;height:23px;background:var(--blue);display:flex;flex-direction:column;justify-content:center;align-items:center;gap:2.5px}
.burger i{display:block;width:12px;height:1.2px;background:var(--white)}
.mobile .welcome{left:10px;top:144px;width:171px;font-size:7.2px;line-height:12.8px;text-align:justify}
.mobile .welcome b{font-size:7.6px}
.mobile .btn{left:51px;top:214px;width:86px;height:20px;font-size:7.5px}
.mobile .band{left:0;top:242px;width:189px;height:160px}
.mobile .band h2{position:absolute;left:0;right:0;top:11px;text-align:center;font-size:7.6px;font-weight:500}
.mobile .row{left:9px;width:171px;height:13px;background:transparent}
.mobile .day{width:53px;padding-left:3px;font-size:7px;clip-path:none}
.mobile .p1{left:65px;width:45px;font-size:6.8px;border-radius:5px}
.mobile .p2{left:121px;width:50px;font-size:6.8px;border-radius:5px}
.mobile .k-title{left:0;right:0;top:418px;text-align:center;font-size:7.5px;font-weight:500;color:#4a4d52}
.mobile .info{left:28px;top:432px;width:133px;height:102px;padding:8px 0 0 13px;font-size:6.6px;line-height:11.2px}
.mobile .map{left:0;top:534px;width:189px;height:132px}
.mobile .footer{top:666px;height:28px;font-size:7.5px}
</style>
</head>
<body>

<!-- Desktop layout -->
<section class="screen desktop">
  <svg class="abs hero-photo" viewBox="0 0 405 314" role="img" aria-label="Foto: Tierärztin untersucht einen Hund auf dem Behandlungstisch">
    <defs><linearGradient id="heroD" x1="0" y1="0" x2="1" y2="1"><stop offset="0" stop-color="#5b8fc4"/><stop offset=".5" stop-color="#c9c3bc"/><stop offset="1" stop-color="#e9e4de"/></linearGradient></defs>
    <path d="M130 0 H405 V314 H95 C40 250 50 120 130 0 Z" fill="url(#heroD)"/>
  </svg>

  <header class="abs header">
    <div class="abs brand"><span class="mark"></span>Dr. Wenzlaff</div>
    <div class="abs phone">
      <svg width="11" height="11" viewBox="0 0 24 24"><path fill="#0a56a8" d="M6.6 10.8a15.1 15.1 0 0 0 6.6 6.6l2.2-2.2a1 1 0 0 1 1-.25 11.4 11.4 0 0 0 3.6.57 1 1 0 0 1 1 1V20a1 1 0 0 1-1 1A17 17 0 0 1 3 4a1 1 0 0 1 1-1h3.5a1 1 0 0 1 1 1c0 1.25.2 2.45.57 3.57a1 1 0 0 1-.25 1z"/></svg>
      030 / 555 12 34
    </div>
  </header>
  <nav class="abs nav">
    <span class="active">HAUPTZEIT</span><span>PRAXIS</span><span>TEAM</span><span>SPRECHZEITEN</span><span style="padding-left:16px">LEISTUNGEN</span><span style="padding-left:16px">KONTAKT/ANFART</span>
  </nav>

  <p class="abs welcome"><b>Herzlich Willkommen</b> auf der Homepage der Tierarztpraxis von Dr. Konrad Wenzlaff. Mein Team und ich haben hier Informationen rund um die Praxis und Hinweise für Patientenbesitzer zusammengestellt.</p>
  <div class="abs btn">Kontaktiere uns</div>

  <section class="abs band">
    <h2>Sprechzeiten ohne Terminvereinbarung</h2>
    <div class="row" style="top:56px"><span class="day">Montag</span><span class="pill p1">9:30-11:00</span><span class="pill p2">16:00-19:00</span></div>
    <div class="row" style="top:81.6px"><span class="day">Dienstag</span><span class="pill p1">9:30-11:00</span><span class="pill p2">16:00-19:00</span></div>
    <div class="row" style="top:107.2px"><span class="day">Mittwoch</span><span class="pill p1">9:30-11:00</span><span class="pill p2">16:00-19:00</span></div>
    <div class="row" style="top:132.8px"><span class="day">Donnerstag</span><span class="pill p2">16:00-19:00</span></div>
    <div class="row" style="top:158.4px"><span class="day">Freitag</span><span class="pill p1">9:30-11:00</span><span class="pill p2">16:00-19:00</span></div>
    <div class="row short" style="top:184px"><span class="day">Samstag</span><span class="pill p1">9:30-11:00</span></div>
  </section>

  <h3 class="abs k-title">Kurzinformation</h3>
  <svg class="abs map" viewBox="0 0 358 251" role="img" aria-label="Karte mit Standort der Praxis">
    <defs><linearGradient id="mapD" x1="0" y1="0" x2="1" y2="1"><stop offset="0" stop-color="#a9cdf2"/><stop offset=".45" stop-color="#dcdcdc"/><stop offset="1" stop-color="#cfd8c4"/></linearGradient></defs>
    <rect width="358" height="251" fill="url(#mapD)"/>
  </svg>
  <address class="abs info" style="font-style:normal">
    Dr. med. vet. Konrad Wenzlaff<br>Fachtierarzt für Kleintiere<br>Lindenhofweg 4b<br><br>12345 Berlin (Waldheim)<br><br>Telefon: 030 / 555 12 34<br>Telefax: 030 / 555 12 35
  </address>
  <footer class="abs footer">Impressum</footer>
</section>

<!-- Mobile layout -->
<section class="screen mobile">
  <div class="abs topbar">
    <svg width="6" height="6" viewBox="0 0 24 24"><path fill="#fff" d="M6.6 10.8a15.1 15.1 0 0 0 6.6 6.6l2.2-2.2a1 1 0 0 1 1-.25 11.4 11.4 0 0 0 3.6.57 1 1 0 0 1 1 1V20a1 1 0 0 1-1 1A17 17 0 0 1 3 4a1 1 0 0 1 1-1h3.5a1 1 0 0 1 1 1c0 1.25.2 2.45.57 3.57a1 1 0 0 1-.25 1z"/></svg>
    030 / 555 12 34
  </div>
  <div class="abs brand"><span class="mark"></span>Dr. Wenzlaff</div>
  <svg class="abs hero-photo" viewBox="0 0 189 90" role="img" aria-label="Foto: Tierärztin untersucht einen Hund">
    <defs><linearGradient id="heroM" x1="0" y1="0" x2="1" y2="1"><stop offset="0" stop-color="#5b8fc4"/><stop offset=".5" stop-color="#c9c3bc"/><stop offset="1" stop-color="#e9e4de"/></linearGradient></defs>
    <path d="M0 0 H120 C160 5 185 40 189 75 V90 H0 Z" fill="url(#heroM)"/>
  </svg>
  <div class="abs burger"><i></i><i></i><i></i></div>

  <p class="abs welcome"><b>Herzlich Willkommen</b> auf der Homepage der Tierarztpraxis von Dr. Konrad Wenzlaff. Mein Team und ich haben hier Informationen rund um die Praxis und Hinweise für Patientenbesitzer zusammengestellt.</p>
  <div class="abs btn">Kontaktiere uns</div>

  <section class="abs band">
    <h2>Sprechzeiten ohne Terminvereinbarung</h2>
    <div class="row" style="top:32px"><span class="day">Montag</span><span class="pill p1">9:30-11:00</span><span class="pill p2">16:00-19:00</span></div>
    <div class="row" style="top:51.7px"><span class="day">Dienstag</span><span class="pill p1">9:30-11:00</span><span class="pill p2">16:00-19:00</span></div>
    <div class="row" style="top:71.4px"><span class="day">Mittwoch</span><span class="pill p1">9:30-11:00</span><span class="pill p2">16:00-19:00</span></div>
    <div class="row" style="top:91.1px"><span class="day">Donnerstag</span><span class="pill p2">16:00-19:00</span></div>
    <div class="row" style="top:110.8px"><span class="day">Freitag</span><span class="pill p1">9:30-11:00</span><span class="pill p2">16:00-19:00</span></div>
    <div class="row" style="top:130.5px"><span class="day">Samstag</span><span class="pill p1">9:30-11:00</span></div>
  </section>

  <h3 class="abs k-title">Kurzinformation</h3>
  <address class="abs info" style="font-style:normal">
    Dr. med. vet. Konrad Wenzlaff<br>Fachtierarzt für Kleintiere<br>Lindenhofweg 4b<br><br>12345 Berlin (Waldheim)<br><br>Telefon: 030 / 555 12 34<br>Telefax: 030 / 555 12 35
  </address>
  <svg class="abs map" viewBox="0 0 189 132" role="img" aria-label="Karte mit Standort der Praxis">
    <defs><linearGradient id="mapM" x1="0" y1="0" x2="1" y2="1"><stop offset="0" stop-color="#a9cdf2"/><stop offset=".45" stop-color="#dcdcdc"/><stop offset="1" stop-color="#cfd8c4"/></linearGradient></defs>
    <rect width="189" height="132" fill="url(#mapM)"/>
  </svg>
  <footer class="abs footer">Impressum</footer>
</section>

</body>
</html>
```